KESTREL RIDGE SPORTS AVIATION CLUB

WE MAKE FLYING FUN AGAIN! We are a Semi Government Sport Aviation club that focuses on the highest quality of aviation training but in the spirit of Sport flying. The club is for aviation enthusiasts to come and share their passion with other club members to build their sport pilot skills.
Club Background and Structure: Club is Semi-Government and falls under the Marlowe Vale Sports Council. We have seven Board Members that Shape the vision of the club. We have a CEO that take care of KRSAC as a whole and an Operations Manager that takes charge of Daily Flight Operations.
SPORT FLYING is different from a normal Pilots license due to the fact that the pilots fly as a hobby and fun and NOT for Commercial purposes . We would like a design to represent a professional but yet fun side of flying to showcase the "club" side (pilot family)
The club focuses on 3 types of Aircraft Fixed wing aircraft, Gyrocopters and Paramotor (NOTE: Paramotor will have their own web page, but the paramotor must be featured as one of the options. when the pilot chooses the paramotor it must link to paramotor web page)
The page must have the following MINIMUM requirements:
1. General page with logo and some nice pictures that feature both aircraft types (photos in files section)
2. "Get Started" tab that features the following sequence a: Choose your aircraft ( picture of Fixed wing and picture of gyrocopter and picture of paramotor)
b: Get a Introductory Flight.
2. "About us"
3. Services & Price
4. Our Team
5. Fleet
6. Bookings (pilots and introductory scenic flights)
7. Events (with calendar please)
8. Contact us
9. FAQ
10 Ground School
11 Other Sports and Activities
12 Our Partners

Requirements
Must have
• Professional design and easy to maintain and user friendlyness
Nice to have
• We have a booking system that needs to be connected to web page if possible
Should not have
• no clip art

```html
<!DOCTYPE html>
<html lang="en">
<head>
<meta charset="utf-8">
<title>Kestrel Ridge Sports Aviation Club</title>
<link href="https://fonts.googleapis.com/css2?family=Roboto:ital,wght@0,300;0,400;0,700;1,700&display=swap" rel="stylesheet">
<style>
:root{
  --blue:#2468d8;
  --violet:#7a3fd2;
  --pink:#ef3e8f;
  --sky:#1f9be6;
  --ink:#1b1b1b;
  --muted:#555;
  --panel:#f2f3f5;
  --white:#fff;
}
*{margin:0;padding:0;box-sizing:border-box}
html,body{width:1200px;height:2672px;overflow:hidden;background:var(--white);font-family:"Roboto",Arial,sans-serif;color:var(--ink)}
.page{position:relative;width:1200px;height:2672px}
.brand{height:240px;display:flex;flex-direction:column;align-items:center;justify-content:center;gap:10px}
.brand-mark{display:flex;align-items:center;gap:14px;font-weight:700;font-size:64px;color:var(--blue);letter-spacing:2px}
.brand-mark i{width:26px;height:26px;border-radius:50%;background:var(--pink);display:block}
.brand-name{font-size:22px;font-weight:700;color:var(--blue);letter-spacing:1px}
.nav{height:140px;background:linear-gradient(90deg,var(--blue),var(--violet));display:flex;flex-direction:column;justify-content:center;align-items:center;gap:22px}
.nav ul{list-style:none;display:flex;gap:26px;align-items:center}
.nav a{color:var(--white);font-style:italic;font-weight:700;font-size:27px;text-decoration:none}
.nav .cta{font-style:normal;background:var(--pink);padding:10px 20px;font-size:24px;letter-spacing:1px}
.hero{height:620px;background:linear-gradient(160deg,#d9e6f2 0%,#9fb3c8 35%,#c8a57a 70%,#b88b5c 100%)}
.section-title{text-align:center;font-weight:700;font-size:40px;margin-top:40px}
.section-title::after{content:"";display:block;width:260px;height:4px;background:var(--ink);margin:10px auto 0}
.copy{padding:0 60px;font-size:17px;line-height:22px;color:var(--ink);margin-top:18px}
.copy + .copy{margin-top:22px}
.aircraft{display:flex;gap:26px;padding:0 60px;margin-top:16px}
.aircraft-card{flex:1;height:312px;display:flex;flex-direction:column;text-decoration:none}
.aircraft-card .photo{flex:1}
.aircraft-card span{height:50px;background:var(--sky);color:var(--white);font-weight:700;font-size:25px;display:flex;align-items:center;justify-content:center}
.photo-wing{background:linear-gradient(180deg,#5aa7e8,#2d7fd0)}
.photo-gyro{background:linear-gradient(180deg,#c6dff2,#d8c7a0)}
.photo-para{background:linear-gradient(180deg,#d9c6a8,#b98e5e)}
.pricing{margin-top:30px;height:520px;background:var(--panel);display:flex;gap:26px;padding:0 80px}
.plan{flex:1;background:var(--white);text-align:center;padding-top:48px}
.plan h3{font-weight:300;font-size:44px}
.plan .label{font-size:15px;color:var(--muted);margin-top:12px}
.plan .amount{font-size:24px;font-weight:700;margin-top:8px}
.plan .desc{font-size:15px;color:var(--muted);margin-top:12px}
.plan .btn{display:inline-block;margin-top:22px;background:var(--sky);color:var(--white);font-size:13px;font-weight:700;padding:12px 26px;letter-spacing:1px}
.plan ul{list-style:none;text-align:left;padding:40px 28px 0}
.plan li{display:flex;align-items:center;gap:14px;font-size:14px;color:var(--muted);height:40px;border-top:1px solid #e4e4e4}
.footer{position:absolute;left:0;top:2380px;width:1200px;height:292px;background:linear-gradient(90deg,var(--blue),var(--violet));color:var(--white)}
.footer-logo{position:absolute;left:160px;top:40px;width:220px;height:140px;background:var(--white);display:flex;flex-direction:column;align-items:center;justify-content:center;gap:6px}
.footer-logo b{font-size:38px;color:var(--blue)}
.footer-logo small{font-size:10px;font-weight:700;color:var(--blue);text-align:center;padding:0 10px}
.col{position:absolute;top:44px;font-size:14px}
.col h4{font-size:14px;letter-spacing:1px;margin-bottom:14px}
.col p{margin-bottom:12px}
.social{display:flex;gap:12px;margin-top:4px}
.social i{width:18px;height:18px;background:var(--white);display:block;border-radius:50%}
.copyright{position:absolute;bottom:14px;width:100%;text-align:center;font-size:13px}
</style>
</head>
<body>
<div class="page">
  <header class="brand">
    <div class="brand-mark"><i></i>KRSAC</div>
    <div class="brand-name">KESTREL RIDGE SPORTS AVIATION CLUB</div>
  </header>
  <nav class="nav">
    <ul><li><a href="#">Home</a></li><li><a href="#">About us</a></li><li><a href="#">Services &amp; Prices</a></li><li><a href="#">Our Team</a></li><li><a href="#">Fleet</a></li><li><a href="#">Bookings</a></li><li><a href="#">Events</a></li><li><a href="#">Contact us</a></li><li><a href="#">Faq</a></li></ul>
    <ul><li><a href="#">Ground School</a></li><li><a href="#">Other Sports &amp; Activities</a></li><li><a href="#">Our Partners</a></li><li><a class="cta" href="#">GET STARTED</a></li></ul>
  </nav>
  <div class="hero" role="img" aria-label="Two pilots flying a gyrocopter over the desert"></div>

  <h2 class="section-title">Sport Aviation</h2>
  <p class="copy">Lorem ipsum dolor sit amet, consectetur adipiscing elit. Suspendisse varius enim in eros elementum tristique. Duis cursus, mi quis viverra ornare, eros dolor interdum nulla, ut commodo diam libero vitae erat. Aenean faucibus nibh et justo cursus id rutrum lorem imperdiet. Nunc ut sem vitae risus tristique posuere.</p>
  <div class="aircraft">
    <a class="aircraft-card" href="#"><div class="photo photo-wing" role="img" aria-label="Fixed wing aircraft in flight"></div><span>Fixed wing aircraft</span></a>
    <a class="aircraft-card" href="#"><div class="photo photo-gyro" role="img" aria-label="Gyrocopter on the airfield"></div><span>Gyrocopters</span></a>
    <a class="aircraft-card" href="#"><div class="photo photo-para" role="img" aria-label="Paramotor pilots over the desert"></div><span>Paramotor</span></a>
  </div>

  <h2 class="section-title">About us</h2>
  <p class="copy">Lorem ipsum dolor sit amet, consectetur adipiscing elit. Suspendisse varius enim in eros elementum tristique. Duis cursus, mi quis viverra ornare, eros dolor interdum nulla, ut commodo diam libero vitae erat. Aenean faucibus nibh et justo cursus id rutrum lorem imperdiet. Nunc ut sem vitae risus tristique posuere.</p>
  <p class="copy">Lorem ipsum dolor sit amet, consectetur adipiscing elit. Suspendisse varius enim in eros elementum tristique. Duis cursus, mi quis viverra ornare, eros dolor interdum nulla, ut commodo diam libero vitae erat. Aenean faucibus nibh et justo cursus id rutrum lorem imperdiet. Nunc ut sem vitae risus tristique posuere.</p>

  <h2 class="section-title">Sevices &amp; Prices</h2>
  <p class="copy">Lorem ipsum dolor sit amet, consectetur adipiscing elit. Suspendisse varius enim in eros elementum tristique. Duis cursus, mi quis viverra ornare, eros dolor interdum nulla, ut commodo diam libero vitae erat. Aenean faucibus nibh et justo cursus id rutrum lorem imperdiet. Nunc ut sem vitae risus tristique posuere.</p>
  <div class="pricing">
    <div class="plan"><h3>Wing Aircraft</h3><p class="label">Price</p><p class="amount">$</p><p class="desc">Lorem ipsum dolor</p><a class="btn" href="#">TRY NOW</a>
      <ul>
        <li><svg width="18" height="18" viewBox="0 0 18 18"><circle cx="9" cy="9" r="8" fill="none" stroke="#333" stroke-width="1.5"/><path d="M5 9l3 3 5-6" fill="none" stroke="#333" stroke-width="1.5"/></svg>Lorem ipsum dolor sit amet</li>
        <li><svg width="18" height="18" viewBox="0 0 18 18"><circle cx="9" cy="9" r="8" fill="none" stroke="#333" stroke-width="1.5"/><path d="M5 9l3 3 5-6" fill="none" stroke="#333" stroke-width="1.5"/></svg>Lorem ipsum dolor sit amet</li>
        <li><svg width="18" height="18" viewBox="0 0 18 18"><circle cx="9" cy="9" r="8" fill="none" stroke="#333" stroke-width="1.5"/><path d="M5 9l3 3 5-6" fill="none" stroke="#333" stroke-width="1.5"/></svg>Lorem ipsum dolor sit amet</li>
        <li><svg width="18" height="18" viewBox="0 0 18 18"><circle cx="9" cy="9" r="8" fill="none" stroke="#333" stroke-width="1.5"/><path d="M5 9l3 3 5-6" fill="none" stroke="#333" stroke-width="1.5"/></svg>Lorem ipsum dolor sit amet</li>
      </ul></div>
    <div class="plan"><h3>Gyrocopters</h3><p class="label">Price</p><p class="amount">$</p><p class="desc">Lorem ipsum dolor</p><a class="btn" href="#">TRY NOW</a>
      <ul>
        <li><svg width="18" height="18" viewBox="0 0 18 18"><circle cx="9" cy="9" r="8" fill="none" stroke="#333" stroke-width="1.5"/><path d="M5 9l3 3 5-6" fill="none" stroke="#333" stroke-width="1.5"/></svg>Etiam sodales ac felis id interdum</li>
        <li><svg width="18" height="18" viewBox="0 0 18 18"><circle cx="9" cy="9" r="8" fill="none" stroke="#333" stroke-width="1.5"/><path d="M5 9l3 3 5-6" fill="none" stroke="#333" stroke-width="1.5"/></svg>Etiam sodales ac felis id interdum</li>
        <li><svg width="18" height="18" viewBox="0 0 18 18"><circle cx="9" cy="9" r="8" fill="none" stroke="#333" stroke-width="1.5"/><path d="M5 9l3 3 5-6" fill="none" stroke="#333" stroke-width="1.5"/></svg>Etiam sodales ac felis id interdum</li>
        <li><svg width="18" height="18" viewBox="0 0 18 18"><circle cx="9" cy="9" r="8" fill="none" stroke="#333" stroke-width="1.5"/><path d="M5 9l3 3 5-6" fill="none" stroke="#333" stroke-width="1.5"/></svg>Etiam sodales ac felis id interdum</li>
      </ul></div>
    <div class="plan"><h3>Paramotor</h3><p class="label">Price</p><p class="amount">$</p><p class="desc">Lorem ipsum dolor</p><a class="btn" href="#">TRY NOW</a>
      <ul>
        <li><svg width="18" height="18" viewBox="0 0 18 18"><circle cx="9" cy="9" r="8" fill="none" stroke="#333" stroke-width="1.5"/><path d="M5 9l3 3 5-6" fill="none" stroke="#333" stroke-width="1.5"/></svg>Etiam sodales ac felis id interdum</li>
        <li><svg width="18" height="18" viewBox="0 0 18 18"><circle cx="9" cy="9" r="8" fill="none" stroke="#333" stroke-width="1.5"/><path d="M5 9l3 3 5-6" fill="none" stroke="#333" stroke-width="1.5"/></svg>Etiam sodales ac felis id interdum</li>
        <li><svg width="18" height="18" viewBox="0 0 18 18"><circle cx="9" cy="9" r="8" fill="none" stroke="#333" stroke-width="1.5"/><path d="M5 9l3 3 5-6" fill="none" stroke="#333" stroke-width="1.5"/></svg>Etiam sodales ac felis id interdum</li>
        <li><svg width="18" height="18" viewBox="0 0 18 18"><circle cx="9" cy="9" r="8" fill="none" stroke="#333" stroke-width="1.5"/><path d="M5 9l3 3 5-6" fill="none" stroke="#333" stroke-width="1.5"/></svg>Etiam sodales ac felis id interdum</li>
      </ul></div>
  </div>

  <footer class="footer">
    <div class="footer-logo"><b>KRSAC</b><small>KESTREL RIDGE SPORTS AVIATION CLUB</small></div>
    <div class="col" style="left:540px"><h4>COMPANY</h4><p>Home</p><p>Pricing</p><p>Our Team</p></div>
    <div class="col" style="left:688px"><h4>CONTACT US</h4><p>Phone : +00 555 0142</p><p>Email : hello@kestrelridge.example</p><p>Adress : 12 Airfield Road</p></div>
    <div class="col" style="left:920px"><h4>ABOUT</h4><p>Terms &amp; Conditions</p><p>Privacy policy</p><div class="social"><i></i><i></i><i></i></div></div>
    <p class="copyright">Copyright © 2022</p>
  </footer>
</div>
</body>
</html>
```